Can you make a cool and versatile Tarnel Ventures Powerpoint template?
See www.tarnelventures.co.uk and http://www.linkedin.com/company/tarnel-ventures-ltd/ (on the right) to see how the logos are currently used - with interchangeably white and black backgrounds.
Target Market(s)
Marketing managers, product managers in HR technology, HR consultants
Industry/Entity Type
It Company
Font styles to use
Sans Serif
Requirements
Must have
- Master slide design, fonts, color theme, etc. Ideally two variations - one with white background (using colorful logo), one with a darker background (using black/white logo).

```html
<!DOCTYPE html>
<html lang="en">
<head>
<meta charset="utf-8">
<title>Tarnel Ventures – Presentation Master Slides</title>
<link rel="stylesheet" href="https://fonts.googleapis.com/css2?family=Arimo:wght@700&family=Roboto+Condensed:wght@700&display=swap">
<style>
  :root {
    --canvas: #ffffff;
    --light-texture: #f1f1f1;
    --light-logo-panel: #f7f7f7;
    --light-wordmark: #3a3935;
    --dark-texture: #1f1f1f;
    --dark-logo-panel: #4d4a49;
    --dark-wordmark: #ffffff;
    --accent-dot: #e8742a;
    --globe-blue-deep: #1d2a6b;
    --globe-blue: #4a7fbf;
    --globe-grey-deep: #4a4a4a;
    --globe-grey: #e6e6e6;
  }
  * { margin: 0; padding: 0; box-sizing: border-box; }
  html, body { width: 1200px; height: 1000px; overflow: hidden; background: var(--canvas); }
  .canvas { position: relative; width: 1200px; height: 1000px; }
  .slide { position: absolute; overflow: hidden; background: var(--canvas); }
  .slide--light { left: 27px; top: 60px; width: 621px; height: 480px; }
  .slide--dark { left: 540px; top: 560px; width: 561px; height: 433px; }
  .slide__art { position: absolute; inset: 0; width: 100%; height: 100%; display: block; }
  .logo-panel { position: absolute; display: flex; flex-direction: column; justify-content: flex-end; }
  .slide--light .logo-panel {
    left: 363px; top: 55px; width: 258px; height: 93px;
    background: var(--light-logo-panel); padding: 0 0 13px 11px;
  }
  .slide--dark .logo-panel {
    left: 354px; top: 39px; width: 207px; height: 74px;
    background: var(--dark-logo-panel); padding: 0 0 7px 13px;
  }
  .logo-panel__dot { display: block; border-radius: 50%; margin-bottom: 10px; }
  .slide--light .logo-panel__dot { width: 18px; height: 18px; background: var(--accent-dot); margin-left: 2px; }
  .slide--dark .logo-panel__dot { width: 14px; height: 14px; background: var(--dark-wordmark); margin-left: 2px; margin-bottom: 12px; }
  .logo-panel__name { white-space: nowrap; line-height: 1; }
  .slide--light .logo-panel__name {
    font-family: "Arimo", Arial, sans-serif; font-weight: 700; font-size: 21px;
    color: var(--light-wordmark); text-transform: uppercase;
  }
  .slide--dark .logo-panel__name {
    font-family: "Roboto Condensed", "Arial Narrow", sans-serif; font-weight: 700; font-size: 20px;
    color: var(--dark-wordmark); text-transform: lowercase;
  }
</style>
</head>
<body>
<main class="canvas">

  <section class="slide slide--light" aria-label="Light master slide">
    <svg class="slide__art" viewBox="0 0 621 480" xmlns="http://www.w3.org/2000/svg">
      <defs>
        <linearGradient id="silverBand" x1="0" y1="0" x2="1" y2="0">
          <stop offset="0" stop-color="#f4f6f8"/>
          <stop offset="0.35" stop-color="#eef3f6"/>
          <stop offset="0.55" stop-color="#9fa3a7"/>
          <stop offset="0.7" stop-color="#d8dadb"/>
          <stop offset="0.85" stop-color="#7c7f83"/>
          <stop offset="1" stop-color="#b5b8ba"/>
        </linearGradient>
        <linearGradient id="silverRing" x1="0" y1="0" x2="1" y2="1">
          <stop offset="0" stop-color="#9ea2a6"/>
          <stop offset="0.45" stop-color="#f3f4f5"/>
          <stop offset="1" stop-color="#8d9094"/>
        </linearGradient>
        <radialGradient id="globeBlue" cx="0.45" cy="0.4" r="0.6">
          <stop offset="0" stop-color="var(--globe-blue)"/>
          <stop offset="1" stop-color="var(--globe-blue-deep)"/>
        </radialGradient>
        <filter id="softShadowLight" x="-20%" y="-20%" width="140%" height="160%">
          <feGaussianBlur stdDeviation="10"/>
        </filter>
      </defs>
      <path class="texture-area" d="M0,0 H621 V480 H470 C380,262 180,198 0,198 Z" fill="var(--light-texture)"/>
      <path class="band-shadow" d="M0,232 C170,228 360,290 445,480" fill="none" stroke="#c9cbcd" stroke-width="26" filter="url(#softShadowLight)" opacity="0.8"/>
      <path class="band" d="M0,206 C180,206 376,268 464,480" fill="none" stroke="url(#silverBand)" stroke-width="16"/>
      <circle class="globe-shadow" cx="496" cy="396" r="76" fill="#b9bbbd" filter="url(#softShadowLight)" opacity="0.6"/>
      <circle class="globe-ring" cx="492" cy="388" r="75" fill="url(#silverRing)"/>
      <circle class="globe" cx="492" cy="388" r="62" fill="url(#globeBlue)" role="img" aria-label="Globe illustration showing the Americas"/>
    </svg>
    <div class="logo-panel">
      <span class="logo-panel__dot"></span>
      <span class="logo-panel__name">Tarnel Ventures</span>
    </div>
  </section>

  <section class="slide slide--dark" aria-label="Dark master slide">
    <svg class="slide__art" viewBox="0 0 561 433" xmlns="http://www.w3.org/2000/svg">
      <defs>
        <linearGradient id="copperBand" x1="0" y1="0" x2="1" y2="0">
          <stop offset="0" stop-color="#2a1812"/>
          <stop offset="0.3" stop-color="#a6715a"/>
          <stop offset="0.48" stop-color="#f2bfa4"/>
          <stop offset="0.65" stop-color="#7b4a33"/>
          <stop offset="0.8" stop-color="#3a2016"/>
          <stop offset="1" stop-color="#c58a6c"/>
        </linearGradient>
        <linearGradient id="copperRing" x1="0" y1="0" x2="1" y2="1">
          <stop offset="0" stop-color="#3a2016"/>
          <stop offset="0.45" stop-color="#f0b99c"/>
          <stop offset="0.7" stop-color="#6b3e2b"/>
          <stop offset="1" stop-color="#e7a98a"/>
        </linearGradient>
        <radialGradient id="globeGrey" cx="0.4" cy="0.4" r="0.65">
          <stop offset="0" stop-color="var(--globe-grey)"/>
          <stop offset="1" stop-color="var(--globe-grey-deep)"/>
        </radialGradient>
        <filter id="softShadowDark" x="-20%" y="-20%" width="140%" height="160%">
          <feGaussianBlur stdDeviation="10"/>
        </filter>
      </defs>
      <path class="texture-area" d="M0,0 H561 V433 H400 C330,255 170,185 0,185 Z" fill="var(--dark-texture)"/>
      <path class="band-shadow" d="M0,215 C160,212 320,270 380,433" fill="none" stroke="#cfd1d2" stroke-width="24" filter="url(#softShadowDark)" opacity="0.8"/>
      <path class="band" d="M0,192 C170,186 340,250 405,433" fill="none" stroke="url(#copperBand)" stroke-width="13"/>
      <circle class="globe-shadow" cx="440" cy="355" r="68" fill="#9a9c9e" filter="url(#softShadowDark)" opacity="0.6"/>
      <circle class="globe-ring" cx="445" cy="345" r="67" fill="url(#copperRing)"/>
      <circle class="globe" cx="445" cy="345" r="56" fill="url(#globeGrey)" role="img" aria-label="Greyscale globe illustration showing the Americas"/>
    </svg>
    <div class="logo-panel">
      <span class="logo-panel__dot"></span>
      <span class="logo-panel__name">Tarnel Ventures</span>
    </div>
  </section>

</main>
</body>
</html>
```